Flyer Project for Industrial Company

We need to change an old flyer and update with new information. Could have some updated design elements! Like the second page design. Keep the text the same. I have added some photos that we would like to use and have more.
We would like it to be professional, it is going out in a direct mail so we need it to be eye catching.
Target Market(s)
General Contracors
Industry/Entity Type
industrial services
Font styles to use
Serif
Sans Serif
Colors
EB3D1F
EC4F4E
F09395
F8D3D4
FCEDEE
Requirements
Must have
- Updated design and modern elements

```html
<!DOCTYPE html>
<html lang="en">
<head>
<meta charset="utf-8">
<title>Why Choose HR Talbot</title>
<link rel="stylesheet" href="https://fonts.googleapis.com/css2?family=Montserrat:ital,wght@0,300;0,400;0,500;0,600;0,700;1,300;1,400;1,600;1,700&display=swap">
<style>
:root{
  --red:#e8333b;
  --pink:#f09395;
  --dark:#333333;
  --paper:#ebebeb;
  --ink:#222222;
  --white:#ffffff;
}
*{margin:0;padding:0;box-sizing:border-box}
html,body{width:987px;height:1200px;overflow:hidden;background:var(--paper)}
body{font-family:"Montserrat",sans-serif;color:var(--ink);position:relative}
.hero{position:absolute;left:0;top:0;width:987px;height:310px}
.headline{position:absolute;left:54px;top:313px;font-size:29px;font-weight:700;color:var(--red);letter-spacing:.2px}
.intro{position:absolute;left:55px;top:348px;width:890px;font-size:19.6px;line-height:35.8px;color:var(--ink)}
.quote-mark-open{position:absolute;left:55px;top:544px;font-size:64px;font-weight:700;font-style:italic;color:var(--red);line-height:1}
.quote-text{position:absolute;left:92px;top:554px;width:820px;font-size:17.8px;font-style:italic;font-weight:600;line-height:30.8px;text-align:center}
.quote-mark-close{display:inline-block;font-size:64px;font-weight:700;color:var(--red);line-height:0;vertical-align:-26px;margin-left:14px;font-style:italic}
.attribution{position:absolute;left:575px;top:652px}
.attribution .name{font-size:19px;font-weight:500;color:var(--red)}
.attribution .role{font-size:14.2px;margin-top:2px}
.partner{position:absolute;left:51px;top:693px;width:892px;height:150px}
.partner-title{position:absolute;left:123px;top:709px;font-size:19.5px;font-weight:600;color:var(--white)}
.partner-text{position:absolute;left:90px;top:745px;width:700px;text-align:center;font-size:17.4px;font-style:italic;font-weight:300;line-height:23px;color:var(--red)}
.partner-name{position:absolute;left:478px;top:800px;font-size:17px;font-weight:500;color:var(--white)}
.partner-role{position:absolute;left:478px;top:820px;font-size:13.5px;font-weight:300;color:var(--red)}
.cta-banner{position:absolute;left:51px;top:856px;width:892px;height:46px;background:var(--red);border-radius:4px;color:var(--white);font-size:25.5px;font-weight:500;line-height:46px;padding-left:88px}
.card{position:absolute;top:919px;height:241px;border-radius:22px 22px 0 0;text-align:center;padding-top:10px}
.card.call{left:50px;width:307px;background:var(--pink)}
.card.mail{left:369px;width:300px;background:var(--dark);color:var(--white)}
.card.web{left:679px;width:274px;background:var(--pink)}
.card-icon{width:40px;height:40px;margin:0 auto 12px}
.card h3{font-size:19px;font-weight:700;margin-bottom:6px}
.card p{font-size:18px;line-height:21px;font-weight:500}
.card .phone{font-size:29px;font-weight:500;margin-top:12px;color:#3a3a3a}
.card.mail p{font-size:19px;line-height:22px}
.card .email{font-size:16.5px;margin-top:10px;font-weight:600}
.card .follow{margin-top:10px;font-weight:700}
.socials{display:flex;justify-content:center;gap:8px;margin:4px 0 6px}
.socials span{width:17px;height:17px;border-radius:50%;background:var(--white)}
.card .small{font-size:15.5px}
.footer-line{position:absolute;left:0;top:1160px;width:987px;height:6px;background:linear-gradient(90deg,#c9245f,var(--pink) 50%,var(--red))}
.footer{position:absolute;left:0;top:1166px;width:987px;height:34px;background:var(--dark)}
</style>
</head>
<body>

<svg class="hero" viewBox="0 0 987 310">
  <defs>
    <linearGradient id="silos" x1="0" y1="0" x2="0" y2="1">
      <stop offset="0" stop-color="#9fc1e0"/><stop offset=".6" stop-color="#8a8f94"/><stop offset="1" stop-color="#6e6a62"/>
    </linearGradient>
    <linearGradient id="plant" x1="0" y1="0" x2="0" y2="1">
      <stop offset="0" stop-color="#cfd8e2"/><stop offset=".55" stop-color="#d8c9a9"/><stop offset="1" stop-color="#c23a2c"/>
    </linearGradient>
    <linearGradient id="stadium" x1="0" y1="0" x2="0" y2="1">
      <stop offset="0" stop-color="#7aa3cf"/><stop offset=".45" stop-color="#7f8590"/><stop offset="1" stop-color="#4a4744"/>
    </linearGradient>
  </defs>
  <polygon role="img" aria-label="Photo of steel silos being torn down by a long-reach excavator" fill="url(#silos)" points="0,0 378,0 282,292 0,292"/>
  <polygon role="img" aria-label="Photo of an excavator demolishing a brewery building with a red wall" fill="url(#plant)" points="386,0 540,0 624,130 530,292 290,292"/>
  <polygon role="img" aria-label="Photo of a pile of twisted steel beams in front of a football stadium" fill="url(#stadium)" points="548,0 987,0 987,292 538,292 632,130"/>
  <polyline points="380,0 284,292" stroke="#f28c8e" stroke-width="6" fill="none"/>
  <polyline points="542,0 628,130 534,292" stroke="#e8333b" stroke-width="7" fill="none"/>
  <path d="M572,209 H987 V310 H566 Q553,310 553,297 V228 Q553,209 572,209 Z" fill="#e8333b" opacity=".85"/>
</svg>

<h1 class="headline">WHY CHOOSE HR TALBOT?</h1>
<p class="intro">H.R. Talbot specializes in projects that require unrelenting attention to precision and the highest priority placed on safety. Our dedication to excellence is why we’re the preferred partner for clients for demolition, rigging, environmental, and site work projects. Our long standing relationships with some of the world’s most renowned structural collapse and forensic engineers means your project has the right experts in place from the beginning.</p>

<span class="quote-mark-open">“</span>
<p class="quote-text">HR Talbot did an excellent job leading a very complex demolition project for us. They bring a level of knowledge and confidence that is very reassuring, especially related to their approach to planning and safety. I would highly recommend them!<span class="quote-mark-close">”</span></p>
<div class="attribution">
  <div class="name">Mark Ellison,</div>
  <div class="role">Chief Operating Officer - Redfield Moore Construction</div>
</div>

<svg class="partner" viewBox="0 0 892 150" aria-hidden="true">
  <path d="M8,0 H350 Q360,0 366,10 Q372,28 390,28 H886 Q892,28 892,34 V144 Q892,150 886,150 H6 Q0,150 0,144 V8 Q0,0 8,0 Z" fill="#333333"/>
</svg>
<div class="partner-title">A 20 YEAR PARTNERSHIP</div>
<p class="partner-text">I have worked with H.R. Talbot for twenty years on major emergencies.<br>They are simply the best, I would call no one else.</p>
<div class="partner-name">Paul R Dennings, PhD, PE, SE,</div>
<div class="partner-role">Managing Director - Hale Corbin Partners</div>

<div class="cta-banner">READY TO LEARN MORE ABOUT PARNTERING WITH US?</div>

<section class="card call">
  <svg class="card-icon" viewBox="0 0 40 40" aria-hidden="true"><circle cx="20" cy="20" r="20" fill="#e8333b"/><path d="M13,10 l4,-1 3,6 -2.5,2 q2,5 5.5,6.5 l2,-2.5 6,3 -1,4 q-6,2 -12,-5 q-6,-7 -5,-13 z" fill="#fff"/></svg>
  <h3>GIVE US A CALL</h3>
  <p>Contact our office anytime<br>to discuss your project.</p>
  <p class="phone">888-555-0142</p>
</section>

<section class="card mail">
  <svg class="card-icon" viewBox="0 0 40 40" aria-hidden="true"><circle cx="20" cy="20" r="20" fill="#fff"/><rect x="10" y="13" width="20" height="14" rx="1.5" fill="#e8333b"/><path d="M10.5,14 L20,21.5 29.5,14" stroke="#fff" stroke-width="2" fill="none"/></svg>
  <h3>EMAIL US</h3>
  <p>Contact your HR Talbot<br>Representative directly or<br>you can email us to receive<br>a Representative at:</p>
  <p class="email">Marketing@HRTalbot.com</p>
</section>

<section class="card web">
  <svg class="card-icon" viewBox="0 0 40 40" aria-hidden="true"><circle cx="20" cy="20" r="20" fill="#e8333b"/><g stroke="#fff" stroke-width="1.6" fill="none"><circle cx="20" cy="20" r="10"/><ellipse cx="20" cy="20" rx="4.5" ry="10"/><line x1="10" y1="20" x2="30" y2="20"/><line x1="12" y1="14" x2="28" y2="14"/><line x1="12" y1="26" x2="28" y2="26"/></g></svg>
  <h3>FIND US ONLINE</h3>
  <p>Find us online at:<br>www.HRTalbot.com</p>
  <p class="follow">Follow Us:</p>
  <div class="socials"><span></span><span></span><span></span><span></span></div>
  <p class="small">See recent projects and more!</p>
</section>

<div class="footer-line"></div>
<div class="footer"></div>

</body>
</html>
```